Criação de Papelaria (6 itens) para Beleza
" Somos uma Distribuidora de Cosméticos. Compramos os produtos diretamente das Indústrias e depois revendemos para lojistas em MG e no Norte do Rio. Antes, nós éramos uma distribuidora apenas da marca Vorani (https://www.voranicosmeticos.com.br/). Por esse motivo, utilizávamos uma logo feita pelo marketing deles, nas cores deles, para que as duas logos sempre andassem casadas. Hoje, ampliamos o nosso mix e distribuímos também os produtos da Mirtex ( https://www.mirtex.com.br/) e da henna Sol de Jade. Ou seja, hoje somos efetivamente uma distribuidora de Cosméticos em geral, atendendo os michos de cabelo, pele, maquiagem e unhas. Dessa maneira, criamos uma nova logo, para representar a Distribuidora. "

```html
<!DOCTYPE html>
<html lang="pt-BR">
<head>
<meta charset="utf-8">
<title>Valtera — Pasta Institucional</title>
<link rel="stylesheet" href="https://fonts.googleapis.com/css2?family=Montserrat:wght@300;400;500&display=swap">
<style>
  :root{
    --stage:#e6e7ea;
    --paper:#ffffff;
    --navy-deep:#0c1526;
    --navy:#1a2740;
    --navy-soft:#2a3957;
    --gold:#c9a25a;
    --gold-light:#e6c98a;
    --mist:#dfe3ea;
    --ink-soft:#7c8597;
  }
  *{box-sizing:border-box;margin:0;padding:0}
  html,body{width:1200px;height:1200px;overflow:hidden}
  body{
    background:var(--stage);
    font-family:"Montserrat",sans-serif;
    display:flex;align-items:center;justify-content:center;
  }
  .folder-spread{
    display:flex;width:1000px;height:700px;
    box-shadow:0 20px 50px rgba(0,0,0,.18);
  }
  .folder-page{position:relative;width:500px;height:700px;overflow:hidden}

  /* inner page */
  .folder-inner{background:var(--paper)}
  .inner-logo{position:absolute;top:52px;left:48px;display:flex;align-items:center;gap:10px}
  .logo-dot{width:26px;height:26px;border-radius:50%;background:var(--gold)}
  .inner-logo .brand-block{display:flex;flex-direction:column}
  .inner-logo .brand-name{font-size:22px;font-weight:400;letter-spacing:2px;color:var(--navy)}
  .inner-logo .brand-tagline{font-size:6px;letter-spacing:2px;color:var(--ink-soft);text-transform:uppercase;margin-top:2px}
  .inner-backdrop{position:absolute;left:-90px;top:150px;width:460px;height:460px;border-radius:50%;background:var(--mist);opacity:.45}
  .inner-contact{
    position:absolute;left:0;right:0;bottom:0;height:70px;
    background:linear-gradient(180deg,var(--navy-soft),var(--navy-deep));
    border-top:2px solid var(--gold);
    display:flex;align-items:center;justify-content:space-between;padding:0 30px;
  }
  .contact-item{display:flex;align-items:center;gap:6px;color:#d4d9e3;font-size:8px;font-weight:300;letter-spacing:.3px}
  .contact-icon{width:14px;height:14px;flex:none}

  /* cover */
  .folder-cover{
    background:radial-gradient(ellipse at 55% 35%,var(--navy-soft) 0%,var(--navy) 45%,var(--navy-deep) 100%);
  }
  .cover-logo{position:absolute;top:270px;left:0;right:0;display:flex;justify-content:center;align-items:center;gap:14px}
  .cover-logo .logo-dot{width:44px;height:44px}
  .cover-logo .brand-block{display:flex;flex-direction:column}
  .cover-logo .brand-name{font-size:40px;font-weight:400;letter-spacing:4px;color:#fff;line-height:1}
  .cover-logo .brand-tagline{font-size:9px;letter-spacing:3.2px;color:#b8c0cf;text-transform:uppercase;margin-top:6px}
  .cover-base{position:absolute;left:0;right:0;bottom:0;height:62px;background:var(--navy-deep)}
  .cover-rule{position:absolute;left:0;right:0;bottom:62px;height:2px;
    background:linear-gradient(90deg,transparent,var(--gold) 20%,var(--gold-light) 50%,var(--gold) 80%,transparent)}
  .spine{position:absolute;left:0;top:0;bottom:0;width:6px;background:linear-gradient(90deg,rgba(0,0,0,.35),transparent)}
</style>
</head>
<body>
  <main class="folder-spread">
    <section class="folder-page folder-inner">
      <div class="inner-backdrop"></div>
      <div class="inner-logo">
        <span class="logo-dot"></span>
        <div class="brand-block">
          <span class="brand-name">VALTERA</span>
          <span class="brand-tagline">Distribuidora de Cosméticos</span>
        </div>
      </div>
      <footer class="inner-contact">
        <div class="contact-item">
          <svg class="contact-icon" viewBox="0 0 14 14"><circle cx="7" cy="7" r="7" fill="#c9a25a"/><path d="M7 3.2a2.4 2.4 0 0 0-2.4 2.4C4.6 7.4 7 10.6 7 10.6s2.4-3.2 2.4-5A2.4 2.4 0 0 0 7 3.2z" fill="#0c1526"/></svg>
          <span>Rua das Acácias, 120 - Centro<br>Campos - RJ - CEP 28010-000</span>
        </div>
        <div class="contact-item">
          <svg class="contact-icon" viewBox="0 0 14 14"><circle cx="7" cy="7" r="7" fill="#c9a25a"/><path d="M4.6 3.8l1.4-.3.8 1.8-.9.7a5 5 0 0 0 2.1 2.1l.7-.9 1.8.8-.3 1.4c-3.2.3-5.9-2.4-5.6-5.6z" fill="#0c1526"/></svg>
          <span>(22) 3300-4521</span>
        </div>
        <div class="contact-item">
          <svg class="contact-icon" viewBox="0 0 14 14"><circle cx="7" cy="7" r="7" fill="#c9a25a"/><rect x="3.6" y="4.6" width="6.8" height="4.8" fill="none" stroke="#0c1526" stroke-width="1"/><path d="M3.6 4.6L7 7.3l3.4-2.7" fill="none" stroke="#0c1526" stroke-width="1"/></svg>
          <span>contato@valteracosmeticos.com.br</span>
        </div>
      </footer>
    </section>

    <section class="folder-page folder-cover">
      <div class="spine"></div>
      <div class="cover-logo">
        <span class="logo-dot"></span>
        <div class="brand-block">
          <span class="brand-name">VALTERA</span>
          <span class="brand-tagline">Distribuidora de Cosméticos</span>
        </div>
      </div>
      <div class="cover-rule"></div>
      <div class="cover-base"></div>
    </section>
  </main>
</body>
</html>
```